Design an Elegant Vellora Brand website

I need a webiste design are looking for ideas for a new theme, color scheme, etc. You come up with the general look and feel of the home page and our team will take it from there.
We're only looking for a one (1) page layout which should be fashionable and graphic intensive, but also include the standard homepage links (about us, see our collections, etc)

Target Market(s)

Our customers are fashionable women looking for an animal friendly and environmentally friendly handbag.

Industry/Entity Type

Business

Number of Pages Required

1 page

Font styles to use
Serif
Sans Serif

Requirements
Must have
• Feel free to modify it with different colors or tweaks as you see fit. We are open to all suggestions.
Nice to have

```html
<!DOCTYPE html>
<html lang="en">
<head>
<meta charset="utf-8">
<title>Vellora — Elegant Handbags</title>
<link rel="stylesheet" href="https://fonts.googleapis.com/css2?family=Playfair+Display:wght@400;700;900&family=Poppins:wght@400;600;700&display=swap">
<style>
:root{
  --hero-brown:#4a2c28;
  --hero-brown-dark:#3b221f;
  --hero-sand:#e6c29d;
  --ink:#111111;
  --body:#333333;
  --line:#d9d9d9;
  --paper:#ffffff;
  --mist:#f6f6f6;
  --footer:#0c0c0c;
  --serif:'Playfair Display', Georgia, serif;
  --sans:'Poppins', Arial, sans-serif;
}
*{margin:0;padding:0;box-sizing:border-box}
html,body{width:1200px;height:2652px;overflow:hidden;background:var(--paper)}
body{position:relative;font-family:var(--serif);color:var(--ink)}
ul{list-style:none}

/* hero */
.hero{position:absolute;left:0;top:0;width:1200px;height:506px;overflow:hidden;
  background:linear-gradient(110deg,var(--hero-brown-dark) 0%,var(--hero-brown) 45%,#52322d 68%)}
.hero-sand{position:absolute;left:818px;top:0;width:382px;height:506px;background:linear-gradient(180deg,#e9c6a2,#e3bd95)}
.hero-arc{position:absolute;left:0;top:0}
.hero-bag{position:absolute;left:630px;top:70px;width:370px;height:395px;
  background:radial-gradient(ellipse 48% 50% at 50% 55%,#f3b4a0 0%,#eea58e 45%,rgba(232,150,128,.55) 70%,rgba(232,150,128,0) 100%)}
.brand{position:absolute;left:250px;top:22px;font-family:var(--sans);font-weight:700;font-size:18px;color:#fff;letter-spacing:.5px}
.brand .mark{display:inline-block;width:22px;height:22px;border-radius:50%;background:#fff;vertical-align:-5px;margin-right:10px}
.main-nav{position:absolute;left:455px;top:26px;display:flex;gap:20px}
.main-nav a{font-family:var(--serif);font-weight:700;font-size:11.5px;color:#fff;text-decoration:none}
.hero-phone{position:absolute;left:832px;top:18px;display:flex;align-items:center;gap:14px;color:#fff}
.hero-phone .label{font-size:10px;font-weight:700;text-align:right}
.hero-phone .num{font-size:12.5px;font-weight:700;letter-spacing:.3px}
.hero-title{position:absolute;left:249px;top:166px;font-weight:900;font-size:40px;line-height:50px;color:#fff;letter-spacing:.2px}
.btn-outline-light{position:absolute;left:249px;top:330px;width:109px;height:36px;border:2px solid #fff;color:#fff;
  font-size:10px;font-weight:700;letter-spacing:1px;display:flex;align-items:center;justify-content:center}

/* features */
.feature{position:absolute;top:530px;width:380px;height:165px}
.feature .thumb{position:absolute;left:0;top:0;width:103px;height:134px;
  background:radial-gradient(ellipse 55% 50% at 50% 62%,#1b1b1b 0%,#2a2a2a 55%,rgba(60,60,60,.35) 80%,rgba(255,255,255,0) 100%)}
.feature h3{position:absolute;left:136px;top:20px;font-size:14px;font-weight:700;white-space:nowrap}
.feature p{position:absolute;left:136px;top:47px;width:185px;font-family:var(--sans);font-size:9.5px;line-height:15px;color:var(--body)}
.feature .more{position:absolute;left:136px;top:102px;font-size:11px;font-weight:700}
.divider{position:absolute;top:530px;width:2px;height:145px;background:var(--line)}

/* about */
.about-photo{position:absolute;left:249px;top:759px;width:331px;height:432px;
  background:
    radial-gradient(ellipse 30% 45% at 52% 52%,rgba(30,40,70,.75),rgba(30,40,70,0)),
    linear-gradient(180deg,#4c5565 0%,#7d8aa0 30%,#a6b2c2 55%,#6f7a8c 80%,#8a8d92 100%);
  box-shadow:0 6px 12px rgba(0,0,0,.2)}
.about-card{position:absolute;left:580px;top:826px;width:371px;height:303px;background:#fff;box-shadow:0 4px 16px rgba(0,0,0,.12)}
.about-card h2{position:absolute;left:30px;top:42px;font-size:31px;font-weight:900}
.about-card h4{position:absolute;left:29px;top:89px;width:330px;font-size:16.5px;line-height:22px;font-weight:700}
.about-card p{position:absolute;left:30px;top:151px;width:312px;font-size:8.6px;line-height:15px;color:var(--body)}
.about-card .more{position:absolute;left:30px;top:244px;font-size:11px;font-weight:700}

/* collections */
.collections{position:absolute;left:0;top:1264px;width:1200px;height:845px;background:var(--mist);overflow:hidden}
.deco-left{position:absolute;left:-60px;top:0;width:290px;height:400px;
  background:radial-gradient(ellipse 50% 50% at 45% 50%,#f3c3b3 0%,#f6d2c5 50%,rgba(246,214,202,.5) 75%,rgba(246,246,246,0) 100%)}
.deco-right{position:absolute;left:975px;top:270px;width:280px;height:570px;
  background:radial-gradient(ellipse 50% 50% at 55% 50%,#9a9a9f 0%,#b4adb3 50%,rgba(190,184,190,.5) 75%,rgba(246,246,246,0) 100%)}
.collections h2{position:absolute;left:0;width:1200px;top:36px;text-align:center;font-size:30px;font-weight:900}
.product{position:absolute;width:221px}
.product .img{width:221px;height:230px}
.product h3{margin-top:24px;font-size:13.5px;font-weight:700;white-space:nowrap}
.product p{margin-top:7px;font-family:var(--sans);font-size:9.5px;line-height:15px;color:var(--body)}
.btn-outline-dark{position:absolute;left:546px;top:774px;width:109px;height:36px;border:2px solid var(--ink);
  font-size:9.5px;font-weight:700;letter-spacing:.8px;display:flex;align-items:center;justify-content:center}

/* newsletter */
.newsletter-title{position:absolute;left:0;width:1200px;top:2155px;text-align:center;font-size:30px;font-weight:900}
.newsletter-form{position:absolute;left:335px;top:2235px;width:531px;height:53px;border:1.5px solid #8a8a8a;display:flex;align-items:center}
.newsletter-form .field{flex:1;padding-left:23px;font-size:10px;color:#8a8a8a}
.newsletter-form .sep{width:1.5px;height:33px;background:#333}
.newsletter-form .submit{width:117px;text-align:center;font-size:10px;font-weight:700;letter-spacing:1.5px}

/* footer */
.site-footer{position:absolute;left:0;top:2352px;width:1200px;height:300px;
  background:radial-gradient(ellipse at 75% 30%,#1c1c1c,var(--footer) 60%);color:#fff}
.footer-brand{position:absolute;left:251px;top:40px;width:135px;text-align:center}
.footer-brand .mark{display:block;margin:0 auto 14px;width:36px;height:36px;border-radius:50%;background:#fff}
.footer-brand span{font-family:var(--sans);font-weight:700;font-size:24px;letter-spacing:.5px}
.footer-col{position:absolute;top:56px}
.footer-col h5{font-size:12.5px;font-weight:700;margin-bottom:15px}
.footer-col li{font-size:10px;height:27px;position:relative;padding-left:16px}
.footer-col li::before{content:"";position:absolute;left:2px;top:5px;width:4px;height:4px;border-radius:50%;background:#fff}
.footer-col address{font-style:normal;font-size:10px;line-height:15px}
.footer-col address div{margin-bottom:12px}
.copyright{position:absolute;left:0;width:1200px;top:257px;text-align:center;font-family:var(--sans);font-size:10px}
.copyright b{font-weight:700}
</style>
</head>
<body>

<header class="hero">
  <div class="hero-sand"></div>
  <svg class="hero-arc" width="1200" height="506" aria-hidden="true">
    <defs>
      <linearGradient id="arcFade" x1="0" y1="1" x2="1" y2="0">
        <stop offset="0" stop-color="#fff" stop-opacity=".75"/>
        <stop offset=".5" stop-color="#fff" stop-opacity=".12"/>
        <stop offset="1" stop-color="#fff" stop-opacity=".8"/>
      </linearGradient>
    </defs>
    <circle cx="790" cy="200" r="320" fill="none" stroke="url(#arcFade)" stroke-width="2"/>
  </svg>
  <div class="hero-bag" role="img" aria-label="Pink leather top-handle handbag with charm"></div>
  <div class="brand"><span class="mark"></span>VELLORA</div>
  <nav class="main-nav">
    <a href="#">Home</a><a href="#">About us</a><a href="#">Shop</a><a href="#">Our Collections</a><a href="#">Contact us</a>
  </nav>
  <div class="hero-phone">
    <svg width="18" height="18" viewBox="0 0 24 24" aria-hidden="true"><path fill="#fff" d="M6.6 10.8a15.1 15.1 0 0 0 6.6 6.6l2.2-2.2c.3-.3.7-.4 1-.2 1.1.4 2.3.6 3.6.6.6 0 1 .4 1 1V20c0 .6-.4 1-1 1A17 17 0 0 1 3 4c0-.6.4-1 1-1h3.5c.6 0 1 .4 1 1 0 1.3.2 2.5.6 3.6.1.3 0 .7-.2 1z"/></svg>
    <div><div class="label">Phone Number</div><div class="num">321 54 9876 - 0</div></div>
  </div>
  <h1 class="hero-title">FASHIONABLE<br>WOMEN LOOKING<br>HANDBAG.</h1>
  <div class="btn-outline-light">CONTACT US</div>
</header>

<section class="features">
  <div class="feature" style="left:41px">
    <div class="thumb" role="img" aria-label="Black leather tote bag"></div>
    <h3>Lorem Ipsum is simply dummy</h3>
    <p>Lorem Ipsum is simply dummy text of the printing and typesetting industry. Lorem Ipsum has been the industry's</p>
    <div class="more">Read More</div>
  </div>
  <div class="divider" style="left:400px"></div>
  <div class="feature" style="left:440px">
    <div class="thumb" role="img" aria-label="Black leather tote bag"></div>
    <h3>Lorem Ipsum is simply dummy</h3>
    <p>Lorem Ipsum is simply dummy text of the printing and typesetting industry. Lorem Ipsum has been the industry's</p>
    <div class="more">Read More</div>
  </div>
  <div class="divider" style="left:803px"></div>
  <div class="feature" style="left:840px">
    <div class="thumb" role="img" aria-label="Black leather tote bag"></div>
    <h3>Lorem Ipsum is simply dummy</h3>
    <p>Lorem Ipsum is simply dummy text of the printing and typesetting industry. Lorem Ipsum has been the industry's</p>
    <div class="more">Read More</div>
  </div>
</section>

<section class="about">
  <div class="about-photo" role="img" aria-label="Woman walking down steps outside a glass building, carrying a black handbag"></div>
  <div class="about-card">
    <h2>About us</h2>
    <h4>Lorem Ipsum is simply dummy text of the printing and typesetting industry.</h4>
    <p>Lorem Ipsum is simply dummy text of the printing and typesetting industry. Lorem Ipsum has been the industry's standard dummy text ever since the 1500s, when an unknown printer took a galley of type and scrambled it to make a type specimen book. It has survived not only five centuries, but also the leap into electronic typesetting, remaining essentially unchanged.</p>
    <div class="more">Read More</div>
  </div>
</section>

<section class="collections">
  <div class="deco-left" role="img" aria-label="Pink quilted handbag, decorative"></div>
  <div class="deco-right" role="img" aria-label="Grey and lilac leather handbag, decorative"></div>
  <h2>Our Collections</h2>

  <div class="product" style="left:249px;top:108px">
    <div class="img" role="img" aria-label="Beige handbag set with tassel" style="background:radial-gradient(ellipse 42% 34% at 50% 50%,#b89872 0%,#c9ad88 45%,#e3d3bf 75%,#fff 100%)"></div>
    <h3>Lorem Ipsum is simply dummy</h3>
    <p>Lorem Ipsum is simply dummy text of the<br>printing and typesetting industry.</p>
  </div>
  <div class="product" style="left:490px;top:108px">
    <div class="img" role="img" aria-label="Black leather tote bag" style="background:radial-gradient(ellipse 32% 38% at 50% 52%,#141414 0%,#2a2a2a 45%,#9a9a9a 75%,#fff 100%)"></div>
    <h3>Lorem Ipsum is simply dummy</h3>
    <p>Lorem Ipsum is simply dummy text of the<br>printing and typesetting industry.</p>
  </div>
  <div class="product" style="left:731px;top:108px">
    <div class="img" role="img" aria-label="Green dome handbag" style="background:radial-gradient(ellipse 36% 26% at 50% 50%,#0f6a41 0%,#1f8a5a 45%,#a9cdb9 75%,#fff 100%)"></div>
    <h3>Lorem Ipsum is simply dummy</h3>
    <p>Lorem Ipsum is simply dummy text of the<br>printing and typesetting industry.</p>
  </div>
  <div class="product" style="left:249px;top:432px">
    <div class="img" role="img" aria-label="Magenta tote bag with tassel" style="background:radial-gradient(ellipse 32% 40% at 50% 50%,#8e2356 0%,#b43a72 45%,#e2b1c7 75%,#fff 100%)"></div>
    <h3>Lorem Ipsum is simply dummy</h3>
    <p>Lorem Ipsum is simply dummy text of the<br>printing and typesetting industry.</p>
  </div>
  <div class="product" style="left:490px;top:432px">
    <div class="img" role="img" aria-label="Blush satchel handbag" style="background:radial-gradient(ellipse 34% 28% at 50% 52%,#c58f78 0%,#deb09a 45%,#f0dbd0 75%,#fff 100%)"></div>
    <h3>Lorem Ipsum is simply dummy</h3>
    <p>Lorem Ipsum is simply dummy text of the<br>printing and typesetting industry.</p>
  </div>
  <div class="product" style="left:731px;top:432px">
    <div class="img" role="img" aria-label="Bright blue handbag" style="background:radial-gradient(ellipse 36% 30% at 50% 52%,#0b5cb8 0%,#1a7be0 45%,#a9c9ef 75%,#fff 100%)"></div>
    <h3>Lorem Ipsum is simply dummy</h3>
    <p>Lorem Ipsum is simply dummy text of the<br>printing and typesetting industry.</p>
  </div>

  <div class="btn-outline-dark">VIEW MORE</div>
</section>

<section class="newsletter">
  <h2 class="newsletter-title">Join Our Newsletter</h2>
  <div class="newsletter-form">
    <div class="field">Your Email Address</div>
    <div class="sep"></div>
    <div class="submit">SIGN UP</div>
  </div>
</section>

<footer class="site-footer">
  <div class="footer-brand"><span class="mark"></span><span>VELLORA</span></div>
  <div class="footer-col" style="left:427px">
    <h5>Company</h5>
    <ul><li>About Us</li><li>Shop</li><li>Our Collections</li><li>Contact us</li></ul>
  </div>
  <div class="footer-col" style="left:558px">
    <h5>Help</h5>
    <ul><li>Email Us</li><li>Help &amp; FAQ</li><li>Make a Return</li><li>Shipping Policy</li><li>Gift Cards</li></ul>
  </div>
  <div class="footer-col" style="left:684px">
    <h5>Quick Links</h5>
    <ul><li>Terms &amp; Conditions</li><li>Privacy Policy</li><li>Affiliates</li><li>Return Policy</li></ul>
  </div>
  <div class="footer-col" style="left:838px">
    <h5>Contact Us</h5>
    <address>
      <div>12 Linden Row #4410<br>IL 60990, Usa</div>
      <div>hello@vellora.com</div>
      <div>321 54 9876 - 0</div>
    </address>
  </div>
  <div class="copyright">© 2020 <b>Vellora</b>. All rights reserved</div>
</footer>

</body>
</html>
```